Marlow Vane Lettings Web Site Design

I am after a very simple 3 page web site please. I attach a PDF with the text and information. The logo is also in the PDF. The colours should be orange and blues. The pages should be HOME - LANDLORDS - TENANTS.
Lettings and Property Management Company aimed at just being a reference point for tenants but more of a sales pitch to landlords. Please refer to the attached PDF and word file which contains far more content for the various pages.

Target Market(s)

Prospective Landlords mainly but tenants also

Industry/Entity Type

Lettings and Property Management

Number of Pages Required

3 page

Font styles to use
Sans Serif
Other font styles liked:
• Candara

Colors
0054AA
0677BA
7BADD7
CADEEF
E8F1F8
F0912C
F2A743
F7CA91
FBE8D2
FDF5EE

Requirements
Must have
• Must be colour co-ordinated to the logo (orange and dark blue predominently, Must have good quality stock images relating to property and renting out property. Should have home page and links to landlord page and tenant page. Must have the 4 logos that we are affiliated to (TKR, Housing Settle, BWN and Tenure Funds Guard) - all attached.
Nice to have
• Modern feel, crisp and sharp but simple - good stock images.

```html
<!DOCTYPE html>
<html lang="en">
<head>
<meta charset="utf-8">
<title>Marlow Vane Lettings – Property Management</title>
<link href="https://fonts.googleapis.com/css2?family=Montserrat:wght@400;500;600;700;800&family=Lato:wght@400;700&display=swap" rel="stylesheet">
<style>
:root{
  --navy:#1f2f6e;
  --orange:#f0912c;
  --blue:#0677ba;
  --sky:#2ea6d9;
  --ink:#1d1d1f;
  --muted:#555a66;
  --line:#d9dde6;
  --pale:#f4f5f8;
  --badge:#cfd5e0;
  --white:#fff;
}
*{box-sizing:border-box;margin:0;padding:0}
html,body{width:1200px;height:3992px;overflow:hidden}
body{font-family:"Montserrat",sans-serif;color:var(--ink);background:var(--white);position:relative}
a{color:inherit;text-decoration:none}
.btn{display:inline-block;font-weight:700;font-size:11px;letter-spacing:.4px;text-transform:uppercase;padding:9px 18px;border-radius:3px;background:var(--orange);color:var(--white)}
.btn.ghost{background:var(--white);color:var(--orange)}
.section-title{font-weight:700;font-size:26px;letter-spacing:.5px;text-transform:uppercase;text-align:center}

.site-header{position:absolute;top:0;left:0;width:1200px;height:73px;background:var(--white);z-index:5}
.brand{position:absolute;left:112px;top:18px;display:flex;align-items:center;gap:8px}
.brand .dot{width:26px;height:26px;border-radius:50%;background:var(--orange)}
.brand span{font-weight:700;font-size:13px;color:var(--navy);line-height:1.1;width:90px}
.nav{position:absolute;left:482px;top:28px;display:flex;gap:32px;font-size:11px;font-weight:600;text-transform:uppercase}
.nav .active{color:var(--orange)}
.site-header .btn{position:absolute;left:952px;top:20px;padding:10px 20px}

.hero{position:absolute;top:73px;left:0;width:1200px;height:540px;background:linear-gradient(180deg,#2c3b78 0%,#3b4a86 35%,#2a3463 70%,#1a2147 100%)}
.hero-curve{position:absolute;left:0;top:560px;width:1200px;height:60px}
.hero-copy{position:absolute;top:140px;left:0;width:1200px;text-align:center;color:var(--white)}
.hero-copy h1{font-weight:800;font-size:52px;line-height:1.02}
.hero-copy p{font-size:12px;font-weight:500;width:620px;margin:16px auto 0;line-height:1.4}
.hero-copy .actions{margin-top:24px;display:flex;gap:14px;justify-content:center}
.hero-copy .btn{padding:10px 20px}

.features{position:absolute;top:552px;left:112px;display:flex;gap:19px}
.feature{width:230px;height:150px;background:var(--white);text-align:center;padding-top:22px;clip-path:polygon(0 0,100% 0,100% 84%,50% 100%,0 84%);box-shadow:0 4px 12px rgba(0,0,0,.1)}
.feature svg{width:36px;height:36px}
.feature h3{font-size:13px;font-weight:600;color:var(--navy);margin-top:6px;font-family:"Lato",sans-serif}
.feature p{font-size:10px;color:var(--muted);line-height:1.3;margin:4px auto 0;width:170px;font-family:"Lato",sans-serif}

.about-media{position:absolute;top:775px;left:112px;width:452px;height:350px}
.about-media .frame{position:absolute;left:0;top:45px;width:420px;height:305px;border-radius:14px;background:var(--orange)}
.about-media .photo{position:absolute;left:10px;top:0;width:390px;height:335px;border-radius:12px;background:linear-gradient(135deg,#e9e4da,#b9a58f 55%,#7d6d60)}
.about-media .doc{position:absolute;left:285px;top:205px;width:165px;height:130px;border-radius:10px;background:linear-gradient(135deg,#f4f1ea,#d8cfc1);border:4px solid var(--white)}
.about-copy{position:absolute;top:818px;left:616px;width:420px}
.about-copy h2{font-weight:700;font-size:26px}
.about-copy p{font-size:11px;color:var(--muted);line-height:1.45;margin-top:10px}
.about-copy .btn{margin-top:14px;padding:10px 20px}

.services{position:absolute;top:1189px;left:0;width:1200px;height:516px;background:var(--navy)}
.services .section-title{color:var(--white);position:absolute;top:50px;width:1200px}
.svc{position:absolute;top:103px;width:478px;color:var(--white)}
.svc .photo{height:200px}
.svc h3{font-size:22px;font-weight:600;margin-top:12px}
.svc ul{list-style:none;margin-top:6px;font-size:11px;line-height:1.6;color:#e4e7f1}
.svc li::before{content:"";display:inline-block;width:5px;height:5px;border-radius:50%;background:var(--white);margin-right:6px;vertical-align:middle}
.svc .btn{margin-top:16px;padding:9px 18px}
.svc-badge{position:absolute;left:552px;top:155px;width:96px;height:90px;border-radius:16px;background:var(--white);display:flex;align-items:center;justify-content:center;text-align:center;font-size:11px;font-weight:700;color:var(--navy)}

.properties .section-title{position:absolute;top:1758px;width:1200px}
.prop-row{position:absolute;top:1810px;left:112px;display:flex;gap:18px}
.prop{width:313px;height:375px;background:var(--white);box-shadow:0 3px 12px rgba(0,0,0,.1)}
.prop .photo{height:187px}
.prop .body{padding:16px 18px}
.prop h3{font-size:14px;font-weight:600}
.prop p{font-size:10.5px;color:var(--muted);line-height:1.4;margin-top:8px;height:44px}
.prop .price{color:var(--blue);font-weight:600;font-size:15px;margin-top:6px}
.prop .specs{display:flex;gap:16px;font-size:10px;margin-top:8px;align-items:center}
.prop .foot{border-top:1px solid var(--line);margin-top:10px;padding-top:10px;display:flex;justify-content:space-between;align-items:center}
.prop .view{color:var(--orange);font-weight:700;font-size:11px}
.prop .tools{display:flex;gap:5px}
.prop .tools i{width:18px;height:18px;border:1px solid #bbb;display:block}
.arrow{position:absolute;width:24px;height:24px;background:var(--orange);color:var(--white);display:flex;align-items:center;justify-content:center;font-size:13px;font-weight:700;border-radius:2px}
.view-all{position:absolute;top:2215px;left:556px;padding:9px 18px;font-size:10px}

.testi-bg{position:absolute;top:2308px;left:0;width:1200px;height:287px;background:linear-gradient(180deg,#2a3a78,#33418a)}
.testimonials .section-title{position:absolute;top:2428px;width:1200px;color:var(--white)}
.testi-row{position:absolute;top:2482px;left:112px;display:flex;gap:18px}
.testi{width:313px;height:222px;background:var(--white);text-align:center;padding-top:22px;clip-path:polygon(0 0,100% 0,100% 86%,50% 100%,0 86%);box-shadow:0 4px 12px rgba(0,0,0,.1)}
.testi .avatar{width:42px;height:42px;margin:0 auto;background:linear-gradient(180deg,#c9ced8,#6c7384)}
.testi .stars{color:var(--orange);font-size:10px;letter-spacing:1px;margin-top:6px}
.testi p{font-size:11px;color:var(--muted);line-height:1.4;width:220px;margin:6px auto 0}
.testi h4{font-size:11px;font-weight:700;margin-top:10px}
.testi small{display:block;font-size:10px;color:#a7acb7;margin-top:2px}

.faq .section-title{position:absolute;top:2757px;width:1200px}
.faq-item{position:absolute;left:112px;width:976px;border:1px solid var(--line);box-shadow:0 2px 6px rgba(0,0,0,.05);padding:24px 22px;font-size:15px;font-weight:500}
.faq-item::after{content:"+";position:absolute;right:24px;top:18px;font-size:22px;font-weight:300;color:#888}
.faq-item.open::after{content:"–"}
.faq-item p{font-size:11px;color:var(--muted);margin-top:10px;line-height:1.4;width:620px;font-weight:400}

.partners{position:absolute;top:3300px;left:0;width:1200px;height:155px;background:var(--pale);display:flex;justify-content:space-around;align-items:center;padding:0 100px}
.partner{display:flex;align-items:center;gap:10px;font-size:15px;font-weight:600;color:var(--navy)}
.partner i{display:block;width:44px;height:44px;border-radius:6px;background:var(--badge)}

.cta{position:absolute;top:3455px;left:0;width:1200px;height:255px;background:var(--sky);text-align:center;color:var(--white)}
.cta h2{font-size:25px;font-weight:700;line-height:1.25;margin-top:58px;text-transform:uppercase}
.cta p{font-size:11px;width:440px;margin:12px auto 0;line-height:1.4}
.cta .actions{display:flex;gap:12px;justify-content:center;margin-top:20px}

.site-footer{position:absolute;top:3710px;left:0;width:1200px;height:282px;background:var(--navy);color:var(--white)}
.f-col{position:absolute;top:40px;font-size:11px;line-height:1.45}
.f-col h4{font-size:12px;font-weight:700;text-transform:uppercase;margin-bottom:16px}
.f-col ul{list-style:none}
.f-col li{margin-bottom:3px}
.f-brand{left:112px;top:30px;width:200px}
.f-brand .name{display:flex;align-items:center;gap:8px;font-weight:700;font-size:13px;margin-bottom:20px}
.f-brand .name i{display:block;width:26px;height:26px;border-radius:50%;background:var(--orange)}
.contact-line{display:flex;gap:6px;margin-bottom:10px}
.contact-line svg{flex:none;margin-top:2px}
.news input{width:220px;height:30px;border:none;border-radius:3px;padding:0 10px;font-size:10px;font-family:inherit}
.news .field{position:relative;margin-top:12px}
.news .btn{position:absolute;right:3px;top:3px;padding:7px 16px;font-size:10px}
.socials{display:flex;gap:8px;margin-top:18px}
.socials i{display:block;width:22px;height:22px;border:1px solid var(--white);background:var(--blue)}
.copyright{position:absolute;top:250px;left:280px;width:640px;border-top:1px solid #4d5a8d;padding-top:10px;text-align:center;font-size:10px}
</style>
</head>
<body>

<header class="site-header">
  <a class="brand" href="#"><i class="dot"></i><span>Marlow Vane Lettings</span></a>
  <nav class="nav">
    <a class="active" href="#">Home</a><a href="#">About Us</a><a href="#">Landlords</a><a href="#">Tenants</a><a href="#">Contact</a>
  </nav>
  <a class="btn" href="#">Enquire Now</a>
</header>

<section class="hero" role="img" aria-label="Large two-storey family house at dusk with lit windows and a wide lawn"></section>
<svg class="hero-curve" viewBox="0 0 1200 60" preserveAspectRatio="none"><path d="M0 0 Q600 70 1200 0 L1200 60 L0 60Z" fill="#fff"/></svg>
<div class="hero-copy">
  <h1>Smart, Simple &amp; Stress-Free<br>Property Management</h1>
  <p>We help landlords protect their investment, secure reliable tenants, and stay fully compliant—while giving tenants the support they need throughout their tenancy</p>
  <div class="actions"><a class="btn" href="#">For Landlords</a><a class="btn ghost" href="#">For Tenants</a></div>
</div>

<div class="features">
  <div class="feature"><svg viewBox="0 0 36 36" fill="none" stroke="#0677ba" stroke-width="1.6"><circle cx="18" cy="16" r="11"/><path d="M12 17l6-5 6 5v6H12z"/><path d="M10 30h16"/></svg><h3>Fully Managed Service</h3><p>Hands-off property management for busy landlords</p></div>
  <div class="feature"><svg viewBox="0 0 36 36" fill="none" stroke="#0677ba" stroke-width="1.6"><path d="M18 5v10"/><circle cx="18" cy="5" r="2"/><path d="M6 24c4-6 8-6 12-2 4-4 8-4 12 2"/><path d="M10 30h16"/></svg><h3>Trusted &amp; Compliant</h3><p>We follow all legal, financial, and safety regulations</p></div>
  <div class="feature"><svg viewBox="0 0 36 36" fill="none" stroke="#0677ba" stroke-width="1.6"><circle cx="10" cy="10" r="4"/><circle cx="26" cy="10" r="4"/><circle cx="18" cy="26" r="4"/><path d="M13 13l3 9M23 13l-3 9M14 10h8"/></svg><h3>Reliable Communication</h3><p>Fast responses + clear updates for both landlords and tenants</p></div>
  <div class="feature"><svg viewBox="0 0 36 36" fill="none" stroke="#0677ba" stroke-width="1.6"><path d="M6 18L18 7l12 11"/><path d="M9 16v14h18V16"/><circle cx="18" cy="21" r="3"/></svg><h3>Quality Tenants</h3><p>Strong referencing and suitability checks</p></div>
</div>

<section class="about">
  <div class="about-media">
    <div class="frame"></div>
    <div class="photo" role="img" aria-label="Couple reviewing tenancy paperwork with a letting agent in a bright living room"></div>
    <div class="doc" role="img" aria-label="Tenancy agreement document with a set of keys"></div>
  </div>
  <div class="about-copy">
    <h2>ABOUT US</h2>
    <p>We are a professional Lettings and Property Management company dedicated to supporting landlords with reliable, compliant, and hassle-free services. From tenant sourcing and rent collection to inspections and full legal compliance, we take care of every detail so your property is protected and your investment performs at its best.</p>
    <p>For tenants, we provide clear guidance, quick communication, and a straightforward process to ensure every tenancy runs smoothly.</p>
    <p>Fully affiliated with TKR, BWN, Housing Settle Scheme, and Tenure Funds Guard, we deliver a service built on trust, transparency, and professionalism.</p>
    <a class="btn" href="#">Learn More</a>
  </div>
</section>

<section class="services">
  <h2 class="section-title">Our Services</h2>
  <div class="svc" style="left:112px">
    <div class="photo" role="img" aria-label="Hand passing house keys to an open palm" style="background:linear-gradient(135deg,#dfe3ea,#c7b7a6 60%,#a8876b)"></div>
    <h3>Landlord Services</h3>
    <ul><li>Find and vet quality tenants quickly.</li><li>Keep landlords updated with clear communication.</li><li>Manage end-of-tenancy processes smoothly.</li><li>Ensure full legal compliance and safety.</li></ul>
    <a class="btn" href="#">View Landlord Services &nbsp;⟶</a>
  </div>
  <div class="svc" style="left:610px">
    <div class="photo" role="img" aria-label="Letting agent meeting with two tenants at a desk" style="background:linear-gradient(135deg,#5a4b3e,#b69a7d 50%,#d9dde4)"></div>
    <h3>Tenant Resources</h3>
    <ul><li>Tenant sourcing and professional marketing.</li><li>Comprehensive tenant screening and referencing.</li><li>Secure rent collection and financial reporting.</li><li>End-of-tenancy support and deposit management.</li></ul>
    <a class="btn" href="#">View Tenant Information &nbsp;⟶</a>
  </div>
  <div class="svc-badge">Marlow<br>Vane</div>
</section>

<section class="properties">
  <h2 class="section-title">Latest Properties</h2>
  <div class="arrow" style="left:75px;top:1982px">‹</div>
  <div class="arrow" style="left:1101px;top:1982px">›</div>
  <div class="prop-row">
    <article class="prop">
      <div class="photo" role="img" aria-label="Orange A-frame cottage among green trees" style="background:linear-gradient(180deg,#6f8f48,#e7902e 55%,#c96d1e)"></div>
      <div class="body"><h3>Stonebridge Lodge</h3><p>A spacious, character-filled rental offering a blend of traditional charm and contemporary comfort</p><div class="price">£ 215.28/week</div>
      <div class="specs"><span>🛏 1</span><span>🛁 1</span></div>
      <div class="foot"><a class="view" href="#">VIEW →</a><div class="tools"><i></i><i></i><i></i></div></div></div>
    </article>
    <article class="prop">
      <div class="photo" role="img" aria-label="Single-storey suburban home with a lawn at sunset" style="background:linear-gradient(180deg,#f4e6c8,#c9c2b0 55%,#6f8a4a)"></div>
      <div class="body"><h3>Parkside Home</h3><p>A well-maintained property in a quiet residential area, offering both privacy and easy access to daily essentials</p><div class="price">£ 215.28/week</div>
      <div class="specs"><span>🛏 1</span><span>🛁 1</span></div>
      <div class="foot"><a class="view" href="#">VIEW →</a><div class="tools"><i></i><i></i><i></i></div></div></div>
    </article>
    <article class="prop">
      <div class="photo" role="img" aria-label="Yellow weatherboard house with a front veranda" style="background:linear-gradient(180deg,#a7c3e2,#e5c98a 55%,#6d7e45)"></div>
      <div class="body"><h3>Oakview Apartment</h3><p>A stylish, fully updated apartment designed for professionals seeking comfort, convenience, and excellent transport links</p><div class="price">£ 215.28/week</div>
      <div class="specs"><span>🛏 1</span><span>🛁 1</span></div>
      <div class="foot"><a class="view" href="#">VIEW →</a><div class="tools"><i></i><i></i><i></i></div></div></div>
    </article>
  </div>
  <a class="btn view-all" href="#">View All</a>
</section>

<section class="testimonials">
  <div class="testi-bg" role="img" aria-label="Dusky blue backdrop of a residential street"></div>
  <h2 class="section-title">Testimonials</h2>
  <div class="arrow" style="left:75px;top:2582px">‹</div>
  <div class="arrow" style="left:1101px;top:2582px">›</div>
  <div class="testi-row">
    <div class="testi"><div class="avatar" role="img" aria-label="Client portrait"></div><div class="stars">★★★★★</div><p>Marlow Vane Lettings made the entire process effortless. They found excellent tenants quickly and kept me updated at every stage</p><h4>R. Dane</h4><small>Landlord</small></div>
    <div class="testi"><div class="avatar" role="img" aria-label="Client portrait"></div><div class="stars">★★★★★</div><p>A really positive renting experience. The team was friendly, professional, and always responded promptly to any questions I had</p><h4>Mira T.</h4><small>Tenant</small></div>
    <div class="testi"><div class="avatar" role="img" aria-label="Client portrait"></div><div class="stars">★★★★★</div><p>Everything was clearly explained, and the move-in process was smooth. I felt supported throughout my tenancy</p><h4>Owen K.</h4><small>Tenant</small></div>
  </div>
</section>

<section class="faq">
  <h2 class="section-title">Frequently Asked Question</h2>
  <div class="faq-item" style="top:2812px">What happens if a tenant wants to leave early?</div>
  <div class="faq-item open" style="top:2892px">What is included in your full management service?<p>Tenant finding, referencing, rent collection, inspections, maintenance handling, compliance guidance, and end-of-tenancy support.</p></div>
  <div class="faq-item" style="top:3009px">What safety checks are required for landlords?</div>
  <div class="faq-item" style="top:3090px">How soon do landlords receive rent payments?</div>
  <div class="faq-item" style="top:3170px">Do you offer landlord compliance guidance?</div>
</section>

<section class="partners" aria-label="Affiliated schemes">
  <div class="partner"><i></i>TKR</div>
  <div class="partner"><i></i>Housing Settle</div>
  <div class="partner"><i></i>BWN</div>
  <div class="partner"><i></i>Tenure Funds Guard</div>
</section>

<section class="cta">
  <h2>Ready to rent or let your<br>property?</h2>
  <p>We offer professional management, qualified tenants, and complete peace of mind for landlords and renters alike.</p>
  <div class="actions"><a class="btn" href="#">List Your Property</a><a class="btn ghost" href="#">Find a Rental Home</a></div>
</section>

<footer class="site-footer">
  <div class="f-col f-brand">
    <div class="name"><i></i>Marlow Vane Lettings</div>
    <p>Trusted family-run lettings and property management. Professional, transparent, and reliable service for landlords and tenants</p>
  </div>
  <div class="f-col" style="left:415px">
    <h4>Quick Links</h4>
    <ul><li>Home</li><li>About Us</li><li>Landlords</li><li>Tenants</li><li>Terms &amp; Condition</li><li>Privacy Policy</li><li>Log Out</li></ul>
  </div>
  <div class="f-col" style="left:598px;width:210px">
    <h4>Contact</h4>
    <div class="contact-line"><svg width="10" height="12" viewBox="0 0 10 12" fill="none" stroke="#fff"><path d="M5 11S1 7 1 4.5a4 4 0 018 0C9 7 5 11 5 11z"/><circle cx="5" cy="4.5" r="1.4"/></svg><span>48 Harbour Lane<br>Saltmere, West Vale<br>SV4 9QT<br>United Kingdom</span></div>
    <div class="contact-line"><svg width="11" height="11" viewBox="0 0 11 11" fill="none" stroke="#fff"><path d="M2 1h2l1 3-1.5 1a6 6 0 002.5 2.5L7 6l3 1v2c0 .6-.4 1-1 1A9 9 0 011 2c0-.6.4-1 1-1z"/></svg><span>0100 555 0192</span></div>
    <div class="contact-line"><svg width="11" height="9" viewBox="0 0 11 9" fill="none" stroke="#fff"><rect x=".5" y=".5" width="10" height="8"/><path d="M.5 .5l5 4 5-4"/></svg><span>hello@marlowvane.example</span></div>
  </div>
  <div class="f-col news" style="left:867px;width:222px">
    <h4>Newsletter</h4>
    <p>Subscribe for updates, news, and property insights</p>
    <div class="field"><input type="text" placeholder="Your Name"><a class="btn" href="#">Subscribe</a></div>
    <div class="socials"><i aria-label="Social profile"></i><i aria-label="Social profile"></i><i aria-label="Social profile"></i><i aria-label="Social profile"></i></div>
  </div>
  <div class="copyright">© 2025 Marlow Vane Lettings. All Rights Reserved.</div>
</footer>

</body>
</html>
```